Power Point Design - Business and Science consulting firm

We need a Power Point Template to be used by our consultants when visiting clients and/or speaking in seminars. Usually in a corporate environment, we are expecting something elegant , modern which inspires integrity and accountability. We are a consulting firm working on bioeconomy (renewable energy, biofuels, circular economy, etc) , innovation management and business strategy.

More about us:

Vortano is a consulting firm specialized in bioeconomy, innovation and business development. Our clients are technology-based companies and those with a genuine interest in innovation for the prosperity of their businesses. We help our clients generate value by leveraging the synergy of scientific-technological topics with business strategies. Due to our multidisciplinary profile, we can easily interact with different company areas and hierarchy levels. We develop projects with a real commitment to our clients' challenges. We always seek to identify and quickly converge to priority disciplines critical to project execution.

Name
The business name choice was guided by a preference for a short word inspired by elements related to our business. "SY" represents the "Sci", a fragment of the word Science, and "GLIA" was chosen from two strands:
• The Italian word consiglia (recommends);
• The human brain, which is formed not only by the well-known neurons, but also by glial cells that support the nervous system. Without glial cells, neurons would not function properly.
In a way, we at Vortano play the discrete role of glial cells in the nervous system within organizations.

Logo
We were looking for a logo that reflected sustainability. Inspiration was found in Brazilian Indians' culture and their ability to live in harmony with the planet. Our logo was created based on various graphics from Amazon tribes.

Slogan
Ideas for Markets was inspired by our ability to think scientifically and identify the elements needed to help our clients in an agile and effective way. Science for innovative and sustainable solutions.

WHAT IS BIOECONOMY (Agribusiness, Pharmaceutical, Energy): see in files a short video.

OUR WEBSITE DRAFT - on going: https://www.fornimapa.com.br/painel/fornimapa.cad-site/preview/4183

OUR LOGO - TECHNICAL INFORMATION:

Fonts:

. for the company name VORTANO the font is "BlairMdITC TT Medium"

. for the slogan IDEAS FOR MARKETS the font is "Century Gothic"

Colors:

. for the blue color we have Pantone + Solid Coated 299 C
CMYK: 80,18,0,0 / RGB:0,160,223 / HEX: #00A0DF

. for the green color we have Pantone + Solid Coated 369 C
CMYK: 67,12,100,1 / RGB:98,166,10 / HEX: #62A60A

. for the gray color we have Pantone + Solid Coated 431 C
CMYK: 66,52,45,17 / RGB:92,102,111 / HEX: #5C666F

External website to get inspired :

http://qmrvo.tpelkd.org/

Target Market(s)

Our clients are companies from energy and food business. Agribusiness is one of our main focus working close to CEO´s and Directors - consulting and advisory.

Industry/Entity Type

Management Consulting

Font styles to use
Sans Serif

Requirements
Must have
• MULTI PURPOSE - powerpoint template
• Brand nourishment - we are a new company, need to start to build our brand. So, that template is our "elegant introduction" .
• Our logo - find the color balance - avoid "visually polluted" approach.
• Sections: Who we are; Areas we serve; Our founder slide (see attachments); Project Scope; illustrations (elegant clean) available to be used on demand by our consultants - Technology Transfer | Innovation Management | Regulatory Affairs | Consulting & Scientific Advisory aligned with Bioeconomy context.
• Template will be used to generate business , we cannot have a template which makes our identity only Science or only Green oriented. The idea is really to have a professional template which captures our company backbone and communciate well with our market. We play our game in an interface (science and business).
• COLORS - mainly those from our Logo.
Nice to have
• Abstract drawings and/or illustrations from databases - look & feel "environment, strategy, business, sustainability, science & innovation".
• Additional sections we may not map here but it is usual in Institutional & project presentations.
Should not have
• Specific macros or executables which may not run in our customers computers for any reason. We typically give our slides to audiences or customers after meetings.

```html
<!DOCTYPE html>
<html lang="en">
<head>
<meta charset="utf-8">
<title>Vortano – Key Areas We Serve</title>
<link rel="stylesheet" href="https://fonts.googleapis.com/css2?family=Cinzel:wght@600&family=Montserrat:wght@400;600;700;800&display=swap">
<style>
  :root {
    --blue: #00a0df;
    --blue-dark: #0a6f93;
    --green: #5fa634;
    --green-dark: #3f7a22;
    --gray: #5c666f;
    --gray-dark: #3a4148;
    --header-a: #353b41;
    --header-b: #5c666f;
    --page: #e6e6e6;
    --white: #ffffff;
  }
  html, body {
    margin: 0;
    padding: 0;
    width: 1200px;
    height: 1011px;
    overflow: hidden;
    background: var(--page);
  }
  .canvas {
    position: relative;
    width: 1200px;
    height: 1011px;
  }
  .slide {
    position: absolute;
    left: 30px;
    top: 102px;
    width: 1140px;
    height: 807px;
    box-shadow: 0 6px 24px rgba(0,0,0,0.18);
  }
  .slide svg { display: block; width: 100%; height: 100%; }
  .slide-title {
    font-family: "Cinzel", "Trebuchet MS", serif;
    font-weight: 600;
    font-size: 27px;
    letter-spacing: 1.5px;
    fill: var(--white);
  }
  .brand-name {
    font-family: "Montserrat", Arial, sans-serif;
    font-weight: 600;
    font-size: 12px;
    letter-spacing: 1px;
    fill: var(--white);
  }
  .brand-tagline {
    font-family: "Montserrat", Arial, sans-serif;
    font-weight: 600;
    font-size: 4.6px;
    letter-spacing: 0.3px;
    fill: var(--white);
  }
  .ribbon-label {
    font-family: "Montserrat", Arial, sans-serif;
    font-weight: 800;
    font-size: 16px;
    fill: var(--white);
    text-anchor: middle;
  }
  .ribbon-label.compact { font-size: 13.5px; }
  .footer-text {
    font-family: "Montserrat", Arial, sans-serif;
    font-weight: 400;
    font-size: 8.5px;
    fill: var(--white);
  }
  .page-number {
    font-family: "Montserrat", Arial, sans-serif;
    font-weight: 600;
    font-size: 6.5px;
    fill: var(--gray-dark);
    text-anchor: middle;
  }
  .fill-green { fill: var(--green); }
  .fill-green-dark { fill: var(--green-dark); }
  .fill-blue { fill: var(--blue); }
  .fill-blue-dark { fill: var(--blue-dark); }
  .fill-gray { fill: var(--gray); }
  .fill-gray-dark { fill: var(--gray-dark); }
  .icon-disc { fill: var(--white); }
  .icon-line { fill: none; stroke-width: 2; stroke-linecap: round; stroke-linejoin: round; }
  .stroke-green { stroke: var(--green); }
  .stroke-blue { stroke: var(--blue); }
  .stroke-gray { stroke: var(--gray); }
</style>
</head>
<body>
<div class="canvas">
  <div class="slide">
    <svg viewBox="0 0 692 490" xmlns="http://www.w3.org/2000/svg" aria-label="Key areas we serve">
      <defs>
        <radialGradient id="slide-bg" cx="50%" cy="45%" r="70%">
          <stop offset="0%" stop-color="#ffffff"/>
          <stop offset="100%" stop-color="#e3e4e5"/>
        </radialGradient>
        <linearGradient id="header-bg" x1="0" y1="0" x2="1" y2="0">
          <stop offset="0%" stop-color="var(--header-a)"/>
          <stop offset="100%" stop-color="var(--header-b)"/>
        </linearGradient>
        <linearGradient id="chevron-band" x1="0" y1="0" x2="1" y2="0">
          <stop offset="0%" stop-color="#4d5a63"/>
          <stop offset="50%" stop-color="#3f7a6a"/>
          <stop offset="100%" stop-color="#1f87b2"/>
        </linearGradient>
      </defs>

      <!-- slide surface -->
      <rect class="slide-surface" x="0" y="0" width="692" height="490" fill="url(#slide-bg)"/>

      <!-- header -->
      <g class="header">
        <rect x="15" y="16" width="665" height="52" fill="url(#header-bg)"/>
        <text class="slide-title" x="30" y="52">KEY AREAS WE SERVE</text>
        <g class="brand">
          <rect x="497" y="33" width="16" height="16" fill="none" stroke="#ffffff" stroke-width="1.4"/>
          <line x1="522" y1="30" x2="522" y2="53" stroke="#ffffff" stroke-width="0.8"/>
          <text class="brand-name" x="527" y="43">VORTANO</text>
          <text class="brand-tagline" x="527" y="50">IDEAS FOR MARKETS</text>
        </g>
        <rect x="612" y="16" width="68" height="52" fill="url(#chevron-band)" opacity="0.85" role="img" aria-label="Decorative chevron band in grey, green and blue"/>
      </g>

      <!-- Technology Transfer -->
      <g class="ribbon ribbon-technology">
        <path class="fill-green-dark" d="M78 160 L96 160 L88 206 Z"/>
        <path class="fill-green" d="M92 93 H286 A33.5 33.5 0 0 1 286 160 H78 Z"/>
        <text class="ribbon-label" x="178" y="122">TECHNOLOGY</text>
        <text class="ribbon-label" x="178" y="143">TRANSFER</text>
        <circle class="icon-disc" cx="290" cy="126.5" r="24"/>
        <g class="icon-line stroke-green">
          <rect x="276" y="113" width="11" height="9"/>
          <rect x="293" y="131" width="11" height="9"/>
          <path d="M292 117 H303 V125 M300 122 L303 125 L306 122"/>
          <path d="M288 136 H277 V128 M274 131 L277 128 L280 131"/>
        </g>
      </g>

      <!-- Regulatory Affairs -->
      <g class="ribbon ribbon-regulatory">
        <path class="fill-gray-dark" d="M55 275 L73 275 L64 322 Z"/>
        <path class="fill-gray" d="M69 208 H287 A33.5 33.5 0 0 1 287 275 H55 Z"/>
        <text class="ribbon-label" x="168" y="237">REGULATORY</text>
        <text class="ribbon-label" x="168" y="258">AFFAIRS</text>
        <circle class="icon-disc" cx="291" cy="241.5" r="24"/>
        <g class="icon-line stroke-gray">
          <rect x="280" y="228" width="18" height="25" rx="1.5"/>
          <rect x="285" y="225" width="8" height="5" rx="1"/>
          <path d="M284 236 H294 M284 241 H294 M284 246 H289"/>
          <circle cx="299" cy="251" r="5" fill="#ffffff"/>
          <path d="M296.5 251 L298.5 253 L301.5 249"/>
        </g>
      </g>

      <!-- Innovation Management -->
      <g class="ribbon ribbon-innovation">
        <path class="fill-blue-dark" d="M25 387 L44 387 L35 435 Z"/>
        <path class="fill-blue" d="M39 323 H287 A32 32 0 0 1 287 387 H25 Z"/>
        <text class="ribbon-label" x="158" y="350">INNOVATION</text>
        <text class="ribbon-label" x="158" y="371">MANAGEMENT</text>
        <circle class="icon-disc" cx="291" cy="355" r="24"/>
        <g class="icon-line stroke-blue">
          <path d="M279 346 A14 10 0 0 1 303 346"/>
          <circle cx="283" cy="353" r="2.5"/>
          <circle cx="291" cy="350" r="2.8"/>
          <circle cx="299" cy="353" r="2.5"/>
          <path d="M280 366 V360 H286 V366 M287 366 V357 H295 V366 M296 366 V360 H302 V366"/>
        </g>
      </g>

      <!-- Consulting & Scientific Advisory -->
      <g class="ribbon ribbon-consulting">
        <path class="fill-blue-dark" d="M375 160 L393 160 L385 206 Z"/>
        <path class="fill-blue" d="M390 95 H637 A32.5 32.5 0 0 1 637 160 H375 Z"/>
        <text class="ribbon-label" x="498" y="122">CONSULTING &amp;</text>
        <text class="ribbon-label" x="498" y="143">SCIENTIFIC ADVISORY</text>
        <circle class="icon-disc" cx="641" cy="127.5" r="24"/>
        <g class="icon-line stroke-blue">
          <rect x="633" y="113" width="16" height="10" rx="1"/>
          <path d="M629 129 H653"/>
          <path d="M632 129 V141 M650 129 V141"/>
          <circle cx="627" cy="124" r="2.3"/>
          <circle cx="655" cy="124" r="2.3"/>
          <path d="M624 137 V131 H630 M658 137 V131 H652"/>
        </g>
      </g>

      <!-- Bioeconomy -->
      <g class="ribbon ribbon-bioeconomy">
        <path class="fill-green-dark" d="M348 273 L366 273 L358 321 Z"/>
        <path class="fill-green" d="M363 208 H585 A32.5 32.5 0 0 1 585 273 H348 Z"/>
        <text class="ribbon-label compact" x="468" y="230">BIOECONOMY</text>
        <text class="ribbon-label compact" x="468" y="247">(BUSINESS</text>
        <text class="ribbon-label compact" x="468" y="264">DEVELOPMENT)</text>
        <circle class="icon-disc" cx="589" cy="240.5" r="24"/>
        <g class="tree-icon">
          <circle cx="589" cy="234" r="11" class="fill-green"/>
          <rect x="587" y="241" width="4" height="14" class="fill-green"/>
        </g>
      </g>

      <!-- footer -->
      <g class="footer">
        <rect x="14" y="453" width="665" height="27" class="fill-green"/>
        <text class="footer-text" x="54" y="470">Date : 31/10/2014</text>
        <text class="footer-text" x="300" y="467">www.Vortano.com.br</text>
        <path d="M641 459 L661 467 L641 475 Z" fill="#ffffff"/>
        <text class="page-number" x="648" y="469.5">4</text>
      </g>
    </svg>
  </div>
</div>
</body>
</html>
```